Porchlight Gin - Label for new Gin bottle

I am looking for a bottle label for our small batch, handcrafted Gin. We are located in the bay-side city of Frankston (Victoria, Australia). I know I want more of a serious label but am torn between traditional or modern styling.

Label to include;
• Porchlight GIN (name)
• Hand Crafted
• Small Batch
• 40% Vol

Using 700ml VANTA Spirit Bottle - Cork

Requirements
Must have
• Name; Porchlight Gin
Method: Hand Crafted
Batch Size; Small Batch
Alc; 40% Vol
Nice to have
• Maybe a coastal/seaside reference or reference to distilling.

```html
<!DOCTYPE html>
<html lang="en">
<head>
<meta charset="utf-8">
<title>Porchlight Gin – Bottle Label</title>
<link rel="stylesheet" href="https://fonts.googleapis.com/css2?family=UnifrakturCook:wght@700&family=Big+Shoulders+Inline+Display:wght@500&family=Oswald:wght@500;600&family=Open+Sans:wght@700&display=swap">
<style>
  :root {
    --page: #ececec;
    --paper: #ffffff;
    --ink: #2a2622;
    --gold: #b8891f;
    --gold-soft: #e9d9b4;
    --gold-pale: #f6efdf;
    --band-grey: #e6e6e8;
    --pattern-grey: #9a9a9e;
  }
  * { margin: 0; padding: 0; box-sizing: border-box; }
  html, body { width: 1200px; height: 1013px; overflow: hidden; }
  body { background: var(--page); position: relative; }

  .label {
    position: absolute; left: 160px; top: 66px;
    width: 880px; height: 882px;
    background: var(--paper);
    box-shadow: 0 6px 24px rgba(0,0,0,0.08);
  }
  .label > * { position: absolute; }

  .band-grey { left: 0; width: 100%; background: var(--band-grey); }
  .pattern-strip {
    background: repeating-linear-gradient(90deg, var(--pattern-grey) 0 10px, #cfcfd2 10px 22px, var(--paper) 22px 44px);
    opacity: 0.55;
  }
  .scallop-row {
    left: 12px; right: 12px; top: 110px; height: 24px;
    background: linear-gradient(180deg, var(--gold) 0, var(--gold-soft) 60%, var(--paper) 100%);
    opacity: 0.6;
    border-radius: 0 0 12px 12px;
  }

  .small-batch {
    left: 0; width: 100%; top: 166px; text-align: center;
    font: 600 15px/1 "Oswald", sans-serif; letter-spacing: 2px; color: var(--ink);
  }
  .small-batch span { border-bottom: 1.5px solid var(--gold); padding-bottom: 3px; }

  .emblem-area {
    left: 192px; top: 324px; width: 498px; height: 228px;
    background: radial-gradient(ellipse at center, var(--gold-pale) 0%, rgba(246,239,223,0.6) 55%, rgba(255,255,255,0) 75%);
  }

  .brand-name {
    left: 0; width: 100%; top: 188px; text-align: center;
    font: 700 108px/1 "UnifrakturCook", serif; color: var(--ink);
  }
  .product-type {
    left: 0; width: 100%; top: 342px; text-align: center;
    font: 500 120px/1 "Big Shoulders Inline Display", sans-serif; color: var(--ink);
  }
  .volume {
    left: 0; width: 100%; top: 500px; text-align: center;
    font: 600 17px/1 "Oswald", sans-serif; letter-spacing: 2px; color: var(--ink);
  }
  .volume span { border-bottom: 1.5px solid var(--gold); padding-bottom: 3px; }

  .ribbon {
    left: 332px; top: 556px; width: 215px; height: 50px;
    border: 2px solid var(--gold); background: var(--paper);
    transform: rotate(4deg);
    display: flex; align-items: center; justify-content: center;
    font: 700 20px/1 "Open Sans", sans-serif; color: var(--ink);
  }

  .harbour-scene {
    left: 0; width: 100%; top: 618px; height: 134px;
    background: linear-gradient(180deg, var(--paper) 0%, var(--gold-pale) 45%, var(--gold-soft) 75%, var(--gold) 100%);
    opacity: 0.8;
  }

  .wheat { top: 781px; width: 72px; height: 14px; background: linear-gradient(90deg, transparent, var(--ink)); border-radius: 7px; opacity: 0.7; }
  .wheat.right { transform: scaleX(-1); }
  .abv-pill {
    left: 316px; top: 772px; width: 248px; height: 32px;
    border-radius: 16px; background: var(--ink); color: var(--paper);
    display: flex; align-items: center; justify-content: center;
    font: 700 20px/1 "Open Sans", sans-serif; letter-spacing: 4px;
  }
</style>
</head>
<body>
  <main class="label">
    <div class="band-grey" style="top:20px;height:66px;"></div>
    <div class="pattern-strip" role="img" aria-label="Grey floral tile pattern border" style="left:12px;right:12px;top:34px;height:46px;"></div>
    <div class="band-grey" style="top:92px;height:6px;"></div>
    <div class="scallop-row" role="img" aria-label="Row of striped gold scallop ornaments"></div>

    <p class="small-batch"><span>SMALL BATCH</span></p>
    <div class="emblem-area" role="img" aria-label="Faint gold emblem ornament behind the product name"></div>
    <h1 class="brand-name">Porchlight</h1>
    <p class="product-type">GIN</p>
    <p class="volume"><span>700ML</span></p>
    <p class="ribbon">Hand Crafted</p>

    <div class="harbour-scene" role="img" aria-label="Gold line illustration of a bay-side pier with arched bridge, lamps and benches over water"></div>

    <div class="band-grey" style="top:752px;height:10px;"></div>
    <div class="pattern-strip" role="img" aria-label="Grey floral tile pattern border" style="left:12px;width:224px;top:770px;height:36px;"></div>
    <div class="wheat" role="img" aria-label="Wheat sprig ornament" style="left:240px;"></div>
    <p class="abv-pill">40%Vol</p>
    <div class="wheat right" role="img" aria-label="Wheat sprig ornament" style="left:568px;"></div>
    <div class="pattern-strip" role="img" aria-label="Grey floral tile pattern border" style="left:644px;width:224px;top:770px;height:36px;"></div>
    <div class="band-grey" style="top:818px;height:18px;"></div>
  </main>
</body>
</html>
```